Banner Ad Design Project

Process description of accounting delivery A to Z

Your folder appointment for delivery of receipts, in and outgoing invoices not necessary but possible – goes into a industrial sized scanner at the office

Electronic delivery via email, Nimbusfil or remote scanning locally at the clients office

Imported into the accounting software (called Ledgrive) with drag and drop from email and Nimbusfil our directly imported from scanner at clients office

Software sets ledger accounts after scanning largely automated
Imported into accounting softer and finished by producing Income statement , Balance sheet and cash flow statements.

Size should fit the www.varnelik.no webpage banners rolling

Target Market(s)

New Clients - its to sell our work as modern

Industry/Entity Type

Accounting

Requirements
Must have
• Color scheme fitting current webpage. Looking for a process driven illustration where details are more 1D not 3D as such. Simplified and easy to grasp scheme of flow in our production pipeline.

```html
<!DOCTYPE html>
<html lang="en">
<head>
<meta charset="utf-8">
<title>Delivery Process Banners</title>
<link rel="stylesheet" href="https://fonts.googleapis.com/css2?family=Hind:wght@400;500;600&display=swap">
<style>
  :root {
    --page: #efefef;
    --panel: #ffffff;
    --ink: #333333;
    --muted: #555555;
    --green: #1f8a6b;
    --rule: #bdbdbd;
    --num: #8a8a8a;
  }
  * { margin: 0; padding: 0; box-sizing: border-box; }
  html, body { width: 1200px; height: 1000px; overflow: hidden; background: var(--page); }
  body { position: relative; font-family: "Hind", Arial, sans-serif; color: var(--ink); }
  .icon-defs { position: absolute; width: 0; height: 0; }

  .banner { position: absolute; left: 216px; width: 768px; height: 240px; background: var(--panel); }
  .banner--en { top: 190px; }
  .banner--no { top: 530px; }

  .banner__title { position: absolute; top: 18px; left: 0; width: 100%; text-align: center; font-size: 17.5px; font-weight: 500; letter-spacing: .1px; }

  .step { position: absolute; display: flex; align-items: flex-start; gap: 6px; }
  .step__num { width: 19px; height: 19px; border: 2px solid var(--num); border-radius: 50%; color: var(--num); font-size: 12px; font-weight: 600; line-height: 16px; text-align: center; flex: none; }
  .step__title { font-size: 14px; line-height: 16px; font-weight: 400; padding-top: 2px; white-space: nowrap; }
  .step__sub { font-size: 10px; line-height: 11px; color: var(--muted); white-space: nowrap; }

  .step--1 { left: 27px; top: 69px; }
  .step--2 { left: 27px; top: 146px; }
  .step--3 { left: 291px; top: 69px; }
  .step--4 { left: 291px; top: 146px; }
  .step--5 { left: 534px; top: 69px; }

  .or { position: absolute; left: 31px; top: 110px; font-size: 13px; }

  .ico { position: absolute; }
  .ico--voucher { left: 113px; top: 103px; width: 29px; height: 34px; }
  .plus { position: absolute; left: 155px; top: 106px; font-size: 17px; font-weight: 600; }
  .ico--scanner { left: 174px; top: 102px; width: 38px; height: 36px; }
  .ico--mail { left: 54px; top: 184px; width: 34px; height: 24px; }
  .storage { position: absolute; left: 106px; top: 185px; display: flex; align-items: center; gap: 5px; font-size: 15px; color: var(--ink); }
  .storage__mark { width: 10px; height: 10px; background: var(--ink); }
  .ico--remote { left: 208px; top: 180px; width: 48px; height: 30px; }

  .brand { position: absolute; left: 361px; top: 104px; width: 94px; height: 26px; display: flex; align-items: center; justify-content: center; gap: 6px; color: var(--green); font-size: 18px; font-weight: 600; }
  .brand__mark { width: 9px; height: 9px; background: var(--green); }

  .ico--stack { left: 360px; top: 179px; width: 32px; height: 37px; }
  .ico--chevrons { left: 400px; top: 190px; width: 17px; height: 14px; }
  .ico--ledger { left: 425px; top: 178px; width: 33px; height: 38px; }

  .ico--report { top: 116px; width: 24px; height: 36px; }
  .ico--report-a { left: 618px; }
  .ico--report-b { left: 655px; width: 28px; }
  .ico--report-c { left: 696px; }

  .divider { position: absolute; top: 72px; height: 140px; border-left: 2px dashed var(--rule); }
  .divider--a { left: 282px; }
  .divider--b { left: 524px; }

  .phase { position: absolute; top: 223px; height: 14px; display: flex; align-items: center; gap: 12px; font-size: 10px; color: var(--muted); }
  .phase::before, .phase::after { content: ""; flex: 1; border-top: 1.5px dashed var(--rule); }
  .phase--1 { left: 32px; width: 236px; }
  .phase--2 { left: 296px; width: 214px; }
  .phase--3 { left: 538px; width: 200px; }

  .flow-arrow { position: absolute; top: 216px; width: 18px; height: 18px; }
  .flow-arrow--a { left: 274px; }
  .flow-arrow--b { left: 516px; }
</style>
</head>
<body>

<svg class="icon-defs" aria-hidden="true">
  <defs>
    <symbol id="i-voucher" viewBox="0 0 29 34">
      <path d="M2 2h25v30H2z" fill="none" stroke="#1f8a6b" stroke-width="2" stroke-dasharray="2 1.2"/>
      <rect x="6" y="6" width="5" height="5" fill="#1f8a6b"/>
      <path d="M6 14h10M6 17h10M6 20h10M6 23h10M6 26h10" stroke="#1f8a6b" stroke-width="1.3"/>
      <text x="18" y="29" font-size="9" font-weight="700" fill="#333" font-family="Arial,sans-serif">$</text>
    </symbol>
    <symbol id="i-scanner" viewBox="0 0 38 36">
      <path d="M3 25l24-22 8 8-24 22z" fill="none" stroke="#333" stroke-width="2.4" stroke-linejoin="round"/>
      <path d="M3 28l8 6 26-24" fill="none" stroke="#333" stroke-width="3.2" stroke-linejoin="round"/>
      <path d="M20 12l-3-8" stroke="#333" stroke-width="2"/>
    </symbol>
    <symbol id="i-mail" viewBox="0 0 34 24">
      <rect x="1.5" y="1.5" width="31" height="21" rx="3" fill="none" stroke="#1f8a6b" stroke-width="2.6"/>
      <path d="M4 4l13 11L30 4" fill="none" stroke="#1f8a6b" stroke-width="2.6"/>
    </symbol>
    <symbol id="i-remote" viewBox="0 0 48 30">
      <rect x="1" y="1" width="34" height="22" rx="1.5" fill="none" stroke="#1f8a6b" stroke-width="2"/>
      <rect x="1" y="18" width="34" height="5" fill="#1f8a6b"/>
      <path d="M14 27h8M16 24v3M20 24v3" stroke="#1f8a6b" stroke-width="2"/>
      <path d="M12 9a8 8 0 0 1 12 0M14.5 11.5a4.5 4.5 0 0 1 7 0" fill="none" stroke="#333" stroke-width="1.6"/>
      <circle cx="18" cy="14" r="1.3" fill="#333"/>
      <rect x="38" y="1" width="9" height="28" rx="1" fill="#1f8a6b"/>
      <rect x="39.5" y="4" width="6" height="21" fill="#fff"/>
    </symbol>
    <symbol id="i-stack" viewBox="0 0 32 37">
      <rect x="1" y="1" width="22" height="28" fill="#fff" stroke="#333" stroke-width="1.5"/>
      <rect x="4" y="4" width="22" height="28" fill="#fff" stroke="#333" stroke-width="1.5"/>
      <rect x="8" y="8" width="22" height="28" fill="#fff" stroke="#333" stroke-width="1.8"/>
      <path d="M11 12h5M11 15h16M11 18h16M11 21h16M11 24h16M11 27h16M11 30h16" stroke="#333" stroke-width="1.4"/>
    </symbol>
    <symbol id="i-chevrons" viewBox="0 0 17 14">
      <path d="M1 1l6 6-6 6M9 1l6 6-6 6" fill="none" stroke="#1f8a6b" stroke-width="3"/>
    </symbol>
    <symbol id="i-ledger" viewBox="0 0 33 38">
      <path d="M2 2h19l8 8v26H2z" fill="#fff" stroke="#1f8a6b" stroke-width="2.2" stroke-linejoin="round"/>
      <path d="M21 2v8h8" fill="#1f8a6b" stroke="#1f8a6b" stroke-width="2"/>
      <path d="M6 10h9M6 14h12M6 18h8" stroke="#1f8a6b" stroke-width="1.4"/>
      <circle cx="24" cy="30" r="6" fill="#fff" stroke="#1f8a6b" stroke-width="2"/>
      <circle cx="24" cy="30" r="2.6" fill="none" stroke="#1f8a6b" stroke-width="1.4"/>
    </symbol>
    <symbol id="i-report-a" viewBox="0 0 24 36">
      <path d="M1.5 1.5h14l7 7v26h-21z" fill="none" stroke="#333" stroke-width="1.8" stroke-linejoin="round"/>
      <path d="M15.5 1.5v7h7" fill="none" stroke="#333" stroke-width="1.5"/>
      <path d="M5 12h6M5 16h6M5 20h6M5 24h6M5 28h6M13 12h2M13 16h2M13 20h2M13 24h2M13 28h2" stroke="#333" stroke-width="1.3"/>
    </symbol>
    <symbol id="i-report-b" viewBox="0 0 28 36">
      <rect x="1" y="1" width="26" height="34" fill="none" stroke="#1f8a6b" stroke-width="1.8"/>
      <rect x="4.5" y="5" width="8" height="6" fill="none" stroke="#1f8a6b" stroke-width="1.4"/>
      <path d="M15 6h9M15 9h9M4.5 15h19.5M4.5 19h19.5M4.5 23h19.5M4.5 27h19.5M4.5 30.5h19.5" stroke="#1f8a6b" stroke-width="1.3"/>
    </symbol>
    <symbol id="i-report-c" viewBox="0 0 24 36">
      <path d="M1.5 1.5h14l7 7v26h-21z" fill="none" stroke="#333" stroke-width="1.8" stroke-linejoin="round"/>
      <path d="M15.5 1.5v7h7" fill="none" stroke="#333" stroke-width="1.5"/>
      <path d="M5 10h8M5 13h8M5 16h8M5 21h14M5 24h14M5 27h14M5 30h14" stroke="#333" stroke-width="1.3"/>
      <text x="14" y="18" font-size="9" font-weight="700" fill="#333" font-family="Arial,sans-serif">$</text>
    </symbol>
    <symbol id="i-flow" viewBox="0 0 18 18">
      <circle cx="9" cy="9" r="7.5" fill="#fff" stroke="#c4c4c4" stroke-width="2"/>
      <path d="M5 9h7M9 5.5L12.5 9 9 12.5" fill="none" stroke="#c4c4c4" stroke-width="2"/>
    </symbol>
  </defs>
</svg>

<section class="banner banner--en" aria-label="Standard and digital delivery process">
  <h2 class="banner__title">Standard &amp; Digital Delivery Process</h2>

  <div class="step step--1"><span class="step__num">1</span><div><p class="step__title">Client delivers vouchers for scanning</p><p class="step__sub">and we prepare them for ledger entry</p></div></div>
  <span class="or">or</span>
  <svg class="ico ico--voucher"><use href="#i-voucher"/></svg>
  <span class="plus">+</span>
  <svg class="ico ico--scanner"><use href="#i-scanner"/></svg>

  <div class="step step--2"><span class="step__num">2</span><div><p class="step__title">Client delivers vouchers electronically</p><p class="step__sub">via email, Nimbusfil or remote scanning</p></div></div>
  <svg class="ico ico--mail"><use href="#i-mail"/></svg>
  <span class="storage"><span class="storage__mark"></span>Nimbusfil</span>
  <svg class="ico ico--remote"><use href="#i-remote"/></svg>

  <div class="divider divider--a"></div>

  <div class="step step--3"><span class="step__num">3</span><div><p class="step__title">Import to accounting software</p><p class="step__sub">directly from scanner or by drag and drop</p></div></div>
  <div class="brand"><span class="brand__mark"></span>Ledgrive</div>

  <div class="step step--4"><span class="step__num">4</span><div><p class="step__title">The software creates ledger</p><p class="step__sub">for each account</p></div></div>
  <svg class="ico ico--stack"><use href="#i-stack"/></svg>
  <svg class="ico ico--chevrons"><use href="#i-chevrons"/></svg>
  <svg class="ico ico--ledger"><use href="#i-ledger"/></svg>

  <div class="divider divider--b"></div>

  <div class="step step--5"><span class="step__num">5</span><div><p class="step__title">Generate reports</p><p class="step__sub">Income statement, balance sheet and<br>Cash flow statement</p></div></div>
  <svg class="ico ico--report ico--report-a"><use href="#i-report-a"/></svg>
  <svg class="ico ico--report ico--report-b"><use href="#i-report-b"/></svg>
  <svg class="ico ico--report ico--report-c"><use href="#i-report-c"/></svg>

  <div class="phase phase--1">Delivery</div>
  <svg class="flow-arrow flow-arrow--a"><use href="#i-flow"/></svg>
  <div class="phase phase--2">Processing</div>
  <svg class="flow-arrow flow-arrow--b"><use href="#i-flow"/></svg>
  <div class="phase phase--3">Finalisation</div>
</section>

<section class="banner banner--no" aria-label="Standard og elektronisk leveringsprosess">
  <h2 class="banner__title">Standard &amp; Elektronisk - leveringsprosess</h2>

  <div class="step step--1"><span class="step__num">1</span><div><p class="step__title">Kunden leverer bilag til skanning</p><p class="step__sub">og vi klargjør for føring</p></div></div>
  <span class="or">eller</span>
  <svg class="ico ico--voucher"><use href="#i-voucher"/></svg>
  <span class="plus">+</span>
  <svg class="ico ico--scanner"><use href="#i-scanner"/></svg>

  <div class="step step--2"><span class="step__num">2</span><div><p class="step__title">Kunden leverer elektronisk</p><p class="step__sub">via email, Nimbusfil eller fjernskanning</p></div></div>
  <svg class="ico ico--mail"><use href="#i-mail"/></svg>
  <span class="storage"><span class="storage__mark"></span>Nimbusfil</span>
  <svg class="ico ico--remote"><use href="#i-remote"/></svg>

  <div class="divider divider--a"></div>

  <div class="step step--3"><span class="step__num">3</span><div><p class="step__title">Importeres til Ledgrive</p><p class="step__sub">direkte fra skanner eller via dra og slipp</p></div></div>
  <div class="brand"><span class="brand__mark"></span>Ledgrive</div>

  <div class="step step--4"><span class="step__num">4</span><div><p class="step__title">Automatisert postering</p><p class="step__sub">for hver konto</p></div></div>
  <svg class="ico ico--stack"><use href="#i-stack"/></svg>
  <svg class="ico ico--chevrons"><use href="#i-chevrons"/></svg>
  <svg class="ico ico--ledger"><use href="#i-ledger"/></svg>

  <div class="divider divider--b"></div>

  <div class="step step--5"><span class="step__num">5</span><div><p class="step__title">Generere rapporter</p><p class="step__sub">Resultat, Balanse og kontantstrøm</p></div></div>
  <svg class="ico ico--report ico--report-a"><use href="#i-report-a"/></svg>
  <svg class="ico ico--report ico--report-b"><use href="#i-report-b"/></svg>
  <svg class="ico ico--report ico--report-c"><use href="#i-report-c"/></svg>

  <div class="phase phase--1">Levere</div>
  <svg class="flow-arrow flow-arrow--a"><use href="#i-flow"/></svg>
  <div class="phase phase--2">Behandle</div>
  <svg class="flow-arrow flow-arrow--b"><use href="#i-flow"/></svg>
  <div class="phase phase--3">Ferdigstille</div>
</section>

</body>
</html>
```